Web page for Gareth Pemblewick Chartered Tax Adviser

I need to take the basic web page that I have created and "Brand it" to be compatible with the corporate logo and stationery created for me by other Studio Flock designers.
I will need a watermark as well as a distinctive home page and then a branded general page for content including a series of Blogs.

Target Market(s)

My practice deals with expatriates including those looking to invest in Australia.

Industry/Entity Type

Crowd

Font styles to use
Other font styles liked:
• Per logo

Requirements
Must have
• Besides the homepage I will need a general page for content, branded in the same style as the letterheads.
Nice to have
• A watermark to go with the blogs and news content.

```html
<!DOCTYPE html>
<html lang="en">
<head>
<meta charset="utf-8">
<title>Gareth Pemblewick – Chartered Tax Adviser</title>
<link href="https://fonts.googleapis.com/css2?family=Noto+Serif:wght@400;700&family=Arimo:wght@400&display=swap" rel="stylesheet">
<style>
:root{
  --navy:#234669;
  --navy-dark:#1a3652;
  --link:#1f4a78;
  --ink:#2b2b2b;
  --body:#666;
  --rule:#e3e3e3;
  --footer:#2a2a2a;
  --footer-text:#d8d8d8;
}
*{margin:0;padding:0;box-sizing:border-box}
html,body{width:752px;height:1200px;overflow:hidden;background:#fff}
body{position:relative;font-family:"Arimo",Arial,sans-serif;color:var(--body)}
.abs{position:absolute}
.serif{font-family:"Noto Serif",Georgia,serif}

.brand{display:flex;align-items:center;gap:6px;color:var(--navy);font-family:"Noto Serif",Georgia,serif}
.brand .mark{width:22px;height:22px;background:var(--navy)}
.brand .name{font-size:12px;line-height:1.05;letter-spacing:.5px}
.brand .name small{display:block;font-size:5.5px;letter-spacing:1.6px}

.nav{top:30px;left:298px;width:392px;display:flex;justify-content:space-between;font-family:"Noto Serif",Georgia,serif;font-size:8px;color:#666}
.nav .active{color:var(--link)}

.hero{left:63px;top:74px;width:625px;height:250px;box-shadow:0 14px 14px -10px rgba(0,0,0,.35);border:1px solid #ddd}
.hero .photo{position:absolute;inset:0;background:linear-gradient(115deg,#1d2d40 0%,#3c5673 35%,#8fa7c2 60%,#dfe8f2 85%,#b9c9dc 100%)}
.hero h1{position:absolute;left:21px;top:76px;font-family:"Noto Serif",Georgia,serif;font-size:24px;color:#fff;font-weight:700}
.hero p{position:absolute;left:21px;top:115px;width:265px;font-family:"Noto Serif",Georgia,serif;font-size:8.5px;line-height:14px;color:#fff}
.btn{display:flex;align-items:center;justify-content:center;background:linear-gradient(#2b5378,var(--navy-dark));color:#fff;font-family:"Noto Serif",Georgia,serif;font-size:8.5px;width:81px;height:27px}
.hero .btn{position:absolute;left:21px;top:155px}
.dots{position:absolute;left:21px;top:223px;display:flex;gap:2px}
.dots i{width:5px;height:5px;background:#fff}
.dots i:first-child{background:var(--navy)}

.welcome{top:362px;left:62px;width:628px;text-align:center}
h2{font-family:"Noto Serif",Georgia,serif;font-size:14.5px;color:var(--ink);font-weight:700}
.welcome p{margin-top:12px;font-size:7.8px;line-height:13px;padding:0 6px}

.service{top:444px;width:110px;text-align:center}
.service svg{display:block;margin:0 auto}
.service h3{margin-top:17px;font-family:"Noto Serif",Georgia,serif;font-size:9.5px;color:var(--ink)}

.rule{left:62px;width:628px;height:1px;background:var(--rule)}

.post-img{width:85px;height:74px;border:1px solid #ddd}
.post h4,.news h4{font-family:"Noto Serif",Georgia,serif;font-size:8.5px;color:var(--ink)}
.post .by{margin-top:8px;font-size:7.8px;color:var(--link)}
.post p,.news p{margin-top:7px;font-size:7.5px;line-height:13px}
.post .comments{margin-top:5px;font-size:7.5px;color:var(--link);display:flex;align-items:center;gap:3px}

.date{width:59px;height:70px;border:1px solid #ddd}
.date .m{height:38px;display:flex;align-items:center;justify-content:center;font-family:"Noto Serif",Georgia,serif;font-weight:700;font-size:11px;color:var(--ink)}
.date .d{height:32px;background:var(--navy);color:#fff;display:flex;align-items:center;justify-content:center;font-size:11px}
.news .more{margin-top:6px;font-size:7.8px;color:var(--link)}

.about p{font-size:7.5px;line-height:13px}

footer{left:0;top:1122px;width:752px;height:78px;background:var(--footer)}
footer .brand{color:#e6e6e6;position:absolute;left:62px;top:14px}
footer .brand .mark{background:#e6e6e6}
.fnav{position:absolute;left:318px;top:20px;width:372px;display:flex;justify-content:space-between;font-size:7.8px;color:var(--footer-text)}
.copy{position:absolute;left:62px;top:52px;font-size:7.8px;color:var(--footer-text)}
.social{position:absolute;left:620px;top:45px;display:flex;gap:2px}
.social i{width:16px;height:16px;border-radius:50%}
</style>
</head>
<body>

<header>
  <div class="abs brand" style="left:62px;top:20px">
    <span class="mark"></span>
    <span class="name">GARETH PEMBLEWICK<small>CHARTERED TAX ADVISER</small></span>
  </div>
  <nav class="abs nav">
    <span class="active">Home</span><span>About Us</span><span>Our Services</span><span>Latest News</span><span>Latest Blog</span><span>Contact Us</span>
  </nav>
</header>

<section class="abs hero">
  <div class="photo" role="img" aria-label="Photo of hands using a tablet showing financial charts"></div>
  <h1>TAX ADVISOR</h1>
  <p>Lorem ipsum dolor sit amet, has falli delectus at. Sint referrentur at sea. Per an ullum dicam percipitur.</p>
  <a class="btn">READ MORE</a>
  <div class="dots"><i></i><i></i><i></i><i></i></div>
</section>

<section class="abs welcome">
  <h2>WELCOME TO GARETH PEMBLEWICK</h2>
  <p>Pro aeque docendi hendrerit eu, per ut prima vivendo invenire, corpora appareat nominati eu eum. Vel no nonumy eligendi adipiscing. Vitae maluisset patrioque mea te, in postea quaerendum vim.Pro aeque docendi hendrerit eu, per ut prima vivendo invenire, corpora appareat nominati eu eum.</p>
</section>

<div class="abs service" style="left:44px">
  <svg width="72" height="62" viewBox="0 0 72 62"><defs><linearGradient id="hx" x1="0" y1="0" x2="0" y2="1"><stop offset="0" stop-color="#2c587f"/><stop offset="1" stop-color="#1b3855"/></linearGradient></defs>
    <polygon points="18,0 54,0 72,31 54,62 18,62 0,31" fill="url(#hx)"/>
    <rect x="24" y="24" width="24" height="17" rx="2" fill="#fff"/><rect x="31" y="20" width="10" height="5" rx="1" fill="none" stroke="#fff" stroke-width="2"/>
    <text x="36" y="37" text-anchor="middle" font-size="11" font-family="Arial" font-weight="700" fill="#234669">$</text></svg>
  <h3>TAX PLANNING</h3>
</div>
<div class="abs service" style="left:223px">
  <svg width="72" height="62" viewBox="0 0 72 62"><polygon points="18,0 54,0 72,31 54,62 18,62 0,31" fill="url(#hx)"/>
    <rect x="24" y="32" width="4" height="9" fill="#fff"/><rect x="30" y="28" width="4" height="13" fill="#fff"/><rect x="36" y="30" width="4" height="11" fill="#fff"/><rect x="42" y="25" width="4" height="16" fill="#fff"/>
    <polyline points="24,27 31,22 37,25 46,19" fill="none" stroke="#fff" stroke-width="1.5"/></svg>
  <h3>ANALYSIS</h3>
</div>
<div class="abs service" style="left:408px">
  <svg width="72" height="62" viewBox="0 0 72 62"><polygon points="18,0 54,0 72,31 54,62 18,62 0,31" fill="url(#hx)"/>
    <text x="27" y="30" text-anchor="middle" font-size="14" font-family="Arial" font-weight="700" fill="#fff">$</text>
    <rect x="32" y="23" width="15" height="20" rx="1" fill="#fff"/><rect x="34" y="25" width="11" height="4" fill="#234669"/>
    <g fill="#234669"><rect x="34" y="31" width="3" height="3"/><rect x="38" y="31" width="3" height="3"/><rect x="42" y="31" width="3" height="3"/><rect x="34" y="35" width="3" height="3"/><rect x="38" y="35" width="3" height="3"/><rect x="42" y="35" width="3" height="3"/></g></svg>
  <h3>BOOK KEEPING</h3>
</div>
<div class="abs service" style="left:588px">
  <svg width="72" height="62" viewBox="0 0 72 62"><polygon points="18,0 54,0 72,31 54,62 18,62 0,31" fill="url(#hx)"/>
    <circle cx="34" cy="32" r="9" fill="none" stroke="#fff" stroke-width="2.5"/><rect x="31" y="19" width="6" height="3" fill="#fff"/>
    <line x1="34" y1="32" x2="34" y2="27" stroke="#fff" stroke-width="2"/><circle cx="44" cy="39" r="4" fill="#fff"/><circle cx="44" cy="39" r="1.5" fill="#234669"/></svg>
  <h3>QUALITY CONTROL</h3>
</div>

<div class="abs rule" style="top:570px"></div>

<h2 class="abs" style="left:61px;top:603px">LATEST BLOG</h2>
<div class="abs post-img" style="left:62px;top:636px;background:linear-gradient(135deg,#c9d6e3,#6f7c8c 55%,#2e3540)" role="img" aria-label="Portrait photo of a smiling businessman"></div>
<div class="abs post" style="left:159px;top:633px;width:200px">
  <h4>LOREM IPSUM DOLOR SIT</h4>
  <div class="by">Posted by Ravi Holt</div>
  <p>In dissentias definitiones vis. Vide facete detraxit ex quo. Sea ex docendi salutatus pertinacia.</p>
  <div class="comments"><svg width="9" height="8" viewBox="0 0 9 8"><ellipse cx="4.5" cy="3.5" rx="4" ry="3" fill="#234669"/><polygon points="2,5 1,8 4,6" fill="#234669"/></svg>0 comments</div>
</div>
<div class="abs post-img" style="left:62px;top:733px;background:linear-gradient(135deg,#e8ecf0,#a9b2bc 50%,#3a3f48)" role="img" aria-label="Photo of a business team meeting at a table"></div>
<div class="abs post" style="left:159px;top:730px;width:200px">
  <h4>LOREM IPSUM DOLOR SIT</h4>
  <div class="by">Posted by Ravi Holt</div>
  <p>In dissentias definitiones vis. Vide facete detraxit ex quo. Sea ex docendi salutatus pertinacia.</p>
  <div class="comments"><svg width="9" height="8" viewBox="0 0 9 8"><ellipse cx="4.5" cy="3.5" rx="4" ry="3" fill="#234669"/><polygon points="2,5 1,8 4,6" fill="#234669"/></svg>0 comments</div>
</div>
<a class="abs btn" style="left:62px;top:828px">VIEW ALL</a>

<h2 class="abs" style="left:396px;top:603px">LATEST NEWS</h2>
<div class="abs date" style="left:396px;top:636px"><div class="m">MAR</div><div class="d">02</div></div>
<div class="abs news" style="left:468px;top:634px;width:222px">
  <h4>PRO AEQUE DOCENDI HENDRERIT</h4>
  <p>Accusamus persecuti cum ea, an constituto dissentiunt cum. Dolor ponderum phaedrum ei eum, eu diam omnes aliquando nec.</p>
  <div class="more">Read More &gt;&gt;</div>
</div>
<div class="abs" style="left:396px;top:721px;width:294px;height:1px;background:var(--rule)"></div>
<div class="abs date" style="left:396px;top:737px"><div class="m">MAR</div><div class="d">31</div></div>
<div class="abs news" style="left:468px;top:735px;width:222px">
  <h4>PRO AEQUE DOCENDI HENDRERIT</h4>
  <p>Accusamus persecuti cum ea, an constituto dissentiunt cum. Dolor ponderum phaedrum ei eum, eu diam omnes aliquando nec.</p>
  <div class="more">Read More &gt;&gt;</div>
</div>
<a class="abs btn" style="left:396px;top:828px">VIEW ALL</a>

<div class="abs rule" style="top:897px"></div>

<h2 class="abs" style="left:61px;top:930px">SHORTLY ABOUT US</h2>
<div class="abs" style="left:62px;top:964px;width:204px;height:110px;border:1px solid #ddd;background:linear-gradient(100deg,#8ea4bb,#c9b8a8 50%,#e6ddd3 75%,#b9c6d2)" role="img" aria-label="Photo of an adviser in conversation with a client"></div>
<div class="abs about" style="left:287px;top:961px;width:403px">
  <p>Lorem ipsum dolor sit amet, has falli delectus at. Sint referrentur at sea. Per an ullum dicam percipitur, no eam sint salutandi, in alterum accusata convenire vel. Ne mei laudem aeterno, eam nostrum ullamcorper at. Doctus epicuri periculis mel at, stet prodesset ei est. Est volutpat corrumpit no, et ipsum idque nec.</p>
  <p style="margin-top:9px">Lorem ipsum dolor sit amet, has falli delectus at. Sint referrentur at sea. Per an ullum dicam percipitur, no eam sint salutandi, in alterum accusata convenire vel. Ne mei laudem aeterno, eam nostrum ullamcorper at.</p>
</div>
<a class="abs btn" style="left:287px;top:1048px">READ MORE</a>

<footer class="abs">
  <div class="brand">
    <span class="mark"></span>
    <span class="name">GARETH PEMBLEWICK<small>CHARTERED TAX ADVISER</small></span>
  </div>
  <nav class="fnav"><span>Home</span><span>/</span><span>About Us</span><span>/</span><span>Our Services</span><span>/</span><span>Latest News</span><span>/</span><span>Latest Blog</span><span>/</span><span>Contact Us</span></nav>
  <div class="copy">Copyright @ 2014 GarethPemblewick.All Rights Reserved.</div>
  <div class="social"><i style="background:#3aa5dc"></i><i style="background:#3b5a9a"></i><i style="background:#e4559a"></i><i style="background:#d7313c"></i></div>
</footer>

</body>
</html>
```